Notary Signing Agent Need Business card Design

Need a Business card design for my new company. RT Belvoni-Strand LLC
Mobile Notary Signing Agent. I go to the customer for closing of Mortgage's Documents . possible signs of honesty, integrity and confidentiality.

Work with Title company to Notary Mortgage closing.

My Target Market is Title companies. Banks and Financial Institution.

Color Blue to Black Professional ) if needed some Green Little Red

And possible a company logo.

Mobile ( travel to clients ) Integrity, Honest Trustworthy. A show of Professional services.

Would like company name and my name on card

Use both sides and front with business name and my name. phone numbers.

Target Market(s)

Title company, Banks mortgage company

Industry/Entity Type

Travel

Contact Information for Business Card

Notary, Certified signing agent, Mobile

Colors
0455a3

Requirements
Must have
• Name of company , owners name phone number,
Nice to have
• blue and black color like a professional look but not limit to these only.
• a stand out from other cards .

```html
<!DOCTYPE html>
<html lang="en">
<head>
<meta charset="utf-8">
<title>RT Belvoni-Strand LLC – Business Card</title>
<link rel="stylesheet" href="https://fonts.googleapis.com/css2?family=Oswald:wght@300;700&family=Montserrat:wght@400;600&display=swap">
<style>
  :root {
    --brand-blue: #0455a3;
    --charcoal: #3a3a3c;
    --paper: #ffffff;
    --silver: #e4e5e7;
    --ink: #2b2b2d;
    --backdrop: #dcdde0;
  }
  html, body {
    margin: 0;
    width: 1200px;
    height: 1000px;
    overflow: hidden;
    background: var(--backdrop);
  }
  .card {
    position: absolute;
    width: 560px;
    height: 320px;
    overflow: hidden;
    box-shadow: 0 10px 26px rgba(0,0,0,.22);
  }
  .card-front { left: 320px; top: 150px; }
  .card-back  { left: 320px; top: 530px; }
  .card-shapes { position: absolute; inset: 0; }

  .company-name {
    position: absolute;
    font-family: "Oswald", sans-serif;
    font-weight: 700;
    color: var(--silver);
    white-space: nowrap;
    letter-spacing: .5px;
  }
  .company-name .suffix { font-weight: 300; margin-left: 8px; }
  .card-front .company-name { left: 0; right: 0; top: 110px; text-align: center; font-size: 46px; }
  .card-back .company-name { left: 26px; top: 256px; font-size: 30px; }

  .contact-strip {
    position: absolute;
    left: 96px; right: 16px; top: 278px;
    display: flex; align-items: center; justify-content: flex-end; gap: 14px;
    font-family: "Montserrat", sans-serif;
    font-size: 14px;
    line-height: 1;
    color: var(--paper);
    letter-spacing: .4px;
    white-space: nowrap;
  }
  .contact-item { display: flex; align-items: center; gap: 6px; flex: none; }
  .dot { width: 6px; height: 6px; border-radius: 50%; background: var(--paper); }

  .owner-name {
    position: absolute;
    left: 350px; top: 60px;
    font-family: "Montserrat", sans-serif;
    font-weight: 600;
    font-size: 17px;
    letter-spacing: 2px;
    color: var(--ink);
    white-space: nowrap;
  }
  .phone-list {
    position: absolute;
    left: 350px; top: 120px;
    margin: 0; padding: 0; list-style: none;
    font-family: "Montserrat", sans-serif;
    font-size: 16px;
    letter-spacing: 1px;
    color: var(--brand-blue);
    white-space: nowrap;
  }
  .phone-list li { display: flex; align-items: center; gap: 10px; margin-bottom: 12px; }
</style>
</head>
<body>

<section class="card card-front" aria-label="Business card front">
  <svg class="card-shapes" width="560" height="320" viewBox="0 0 560 320" aria-hidden="true">
    <rect width="560" height="320" fill="var(--brand-blue)"/>
    <polygon points="300,0 560,0 560,70 470,14" fill="var(--charcoal)"/>
    <polygon points="110,258 560,258 560,320 0,320 0,274" fill="var(--charcoal)"/>
  </svg>
  <div class="company-name">RT Belvoni-Strand<span class="suffix">LLC</span></div>
  <div class="contact-strip">
    <span class="contact-item">
      <svg width="17" height="17" viewBox="0 0 20 20" aria-hidden="true"><polygon points="10,1 18,5.5 18,14.5 10,19 2,14.5 2,5.5" fill="var(--paper)"/><text x="10" y="14" text-anchor="middle" font-family="Montserrat, sans-serif" font-size="10" font-weight="600" fill="var(--brand-blue)">P</text></svg>
      555-201-3847
    </span>
    <span class="contact-item">
      <svg width="17" height="17" viewBox="0 0 20 20" aria-hidden="true"><polygon points="10,1 18,5.5 18,14.5 10,19 2,14.5 2,5.5" fill="var(--paper)"/><text x="10" y="14" text-anchor="middle" font-family="Montserrat, sans-serif" font-size="10" font-weight="600" fill="var(--brand-blue)">F</text></svg>
      555-418-6620
    </span>
    <span class="contact-item"><span class="dot"></span>Daniel R Hartwell</span>
  </div>
</section>

<section class="card card-back" aria-label="Business card back">
  <svg class="card-shapes" width="560" height="320" viewBox="0 0 560 320" aria-hidden="true">
    <rect width="560" height="320" fill="var(--charcoal)"/>
    <polygon points="90,0 250,0 205,140" fill="var(--brand-blue)"/>
    <polygon points="285,0 560,0 560,228 345,192" fill="var(--paper)"/>
    <polygon points="0,150 560,238 560,320 0,320" fill="var(--brand-blue)"/>
  </svg>
  <div class="owner-name">Daniel R Hartwell</div>
  <ul class="phone-list">
    <li>
      <svg width="24" height="24" viewBox="0 0 20 20" aria-hidden="true"><polygon points="10,1 18,5.5 18,14.5 10,19 2,14.5 2,5.5" fill="var(--brand-blue)"/><path d="M7 6.5c.6-.6 1.2-.4 1.5.2l.6 1.2c.2.4 0 .8-.3 1l-.5.4c.4.9 1.1 1.6 2 2l.4-.5c.3-.3.7-.4 1-.2l1.2.6c.6.3.8.9.2 1.5-1.6 1.6-7.7-4.5-6.1-6.2z" fill="var(--paper)"/></svg>
      555-201-3847
    </li>
    <li>
      <svg width="24" height="24" viewBox="0 0 20 20" aria-hidden="true"><polygon points="10,1 18,5.5 18,14.5 10,19 2,14.5 2,5.5" fill="var(--brand-blue)"/><rect x="6" y="8" width="8" height="5" fill="var(--paper)"/><rect x="7.5" y="5.5" width="5" height="2.5" fill="var(--paper)"/></svg>
      555-418-6620
    </li>
  </ul>
  <div class="company-name">RT Belvoni-Strand<span class="suffix">LLC</span></div>
</section>

</body>
</html>
```